5x8" package design for beauty / skin care product in a mylar bag

Brevona Works’ Glycolic Acid Powder is pure glycolic acid powder that, when mixed with water, creates glycolic acid solution. Depending on the amount of water added to the powder, you can create different strengths of the solution. Commerical products use between 10 and 70% glycolic acid solution in products. Brevona Works is part of the Calmora hair care company. One of our products use glycolic acid and we can repurpose the raw ingredient alone for retail sales targeting do-it-yourself at home beauty and skin care makers.

Most sellers of glycolic acid powder use basic packaging. Brevona Works intends to create professional, standout packaging that reinforces the quality of the glycolic acid powder we are selling and is consistent with other Calmora brand products sold.

Package design is for a 5x8" matte finished, top loading, resealable pouch. Just looking for front design initially. Second project will include back pouch design using format or design from the front of package.

```html
<!DOCTYPE html>
<html lang="en">
<head>
<meta charset="utf-8">
<title>Brevona Works Glycolic Acid Powder – Pouch Front</title>
<link href="https://fonts.googleapis.com/css2?family=Montserrat:wght@400;500;700;800&display=swap" rel="stylesheet">
<style>
  :root {
    --stage: #e4e4e4;
    --teal-top: #5a9190;
    --teal-mid: #3a7375;
    --teal-deep: #2c6264;
    --teal-haze: #4f8183;
    --powder-grey: #cfdadd;
    --powder-white: #f4f6f7;
    --olive: #a09a55;
    --white: #ffffff;
    --muted-label: #b9cfcf;
    --formula-ink: #6b7c7c;
    --ink: #1e1e1e;
  }
  html, body {
    margin: 0;
    width: 1200px;
    height: 871px;
    overflow: hidden;
    background: var(--stage);
    font-family: "Montserrat", sans-serif;
  }
  .pouch-front {
    position: absolute;
    left: 351px;
    top: 35px;
    width: 498px;
    height: 800px;
    overflow: hidden;
    background: linear-gradient(180deg, var(--teal-top) 0%, var(--teal-mid) 30%, var(--teal-deep) 60%, var(--teal-deep) 100%);
    box-shadow: 0 10px 18px rgba(0,0,0,0.18);
    color: var(--white);
  }
  .brand-name {
    position: absolute;
    left: 56px;
    top: 40px;
    width: 280px;
    font-weight: 500;
    color: var(--white);
    line-height: 1;
  }
  .brand-name .brand-line-one { display: block; font-size: 80px; letter-spacing: -1px; }
  .brand-name .brand-line-two { display: block; font-size: 50px; letter-spacing: 14px; margin-top: 10px; }
  .product-tag {
    position: absolute;
    left: 328px;
    top: 178px;
    font-weight: 700;
    font-size: 14px;
    line-height: 18px;
    color: var(--muted-label);
  }
  .formula-box {
    display: inline-block;
    margin-top: 2px;
    background: var(--white);
    color: var(--formula-ink);
    font-weight: 400;
    font-size: 12px;
    letter-spacing: 2px;
    padding: 0 16px;
    line-height: 17px;
  }
  .product-title {
    position: absolute;
    left: 0;
    width: 100%;
    top: 240px;
    margin: 0;
    text-align: center;
    font-weight: 800;
    font-size: 78px;
    line-height: 74px;
    letter-spacing: -3px;
  }
  .product-form {
    position: absolute;
    left: 0;
    width: 100%;
    top: 393px;
    text-align: center;
    font-weight: 400;
    font-size: 27px;
    letter-spacing: 3px;
  }
  .uses-band {
    position: absolute;
    left: 0;
    top: 453px;
    width: 100%;
    height: 53px;
    background: var(--olive);
    display: flex;
    align-items: center;
    justify-content: center;
    font-weight: 700;
    font-size: 15.5px;
    z-index: 2;
  }
  .powder-photo {
    position: absolute;
    left: 0;
    top: 506px;
    width: 100%;
    height: 294px;
    background: linear-gradient(180deg, var(--teal-deep) 0%, var(--teal-haze) 40%, var(--powder-grey) 68%, var(--powder-white) 100%);
  }
  .free-from {
    position: absolute;
    left: 44px;
    top: 524px;
    width: 90px;
    z-index: 2;
  }
  .free-from .percent {
    font-weight: 800;
    font-size: 42px;
    line-height: 44px;
    letter-spacing: -1px;
  }
  .free-from ul { list-style: none; margin: 6px 0 0; padding: 0; }
  .free-from li {
    font-size: 16px;
    line-height: 30px;
    border-bottom: 1px solid rgba(255,255,255,0.7);
  }
  .free-from li:last-child { border-bottom: none; }
  .resealable {
    position: absolute;
    left: 371px;
    top: 532px;
    z-index: 2;
    font-size: 16px;
    line-height: 18px;
  }
  .resealable svg { display: block; margin: 0 0 10px 3px; }
  .net-weight {
    position: absolute;
    left: 0;
    width: 100%;
    top: 752px;
    text-align: center;
    font-size: 15px;
    font-weight: 500;
    color: var(--ink);
    z-index: 2;
  }
</style>
</head>
<body>
  <main class="pouch-front">
    <div class="brand-name">
      <span class="brand-line-one">Brevona</span>
      <span class="brand-line-two">WORKS</span>
    </div>
    <div class="product-tag">
      GLYCOLIC<br>ACID POWDER<br>
      <span class="formula-box">C₂H₄O₃</span>
    </div>

    <h1 class="product-title">GLYCOLIC<br>ACID</h1>
    <div class="product-form">-POWDER-</div>

    <div class="uses-band">Facial | Toner | Scalp Scrub | Hyperpigmentation</div>

    <div class="powder-photo" role="img" aria-label="Photo of a heap of white glycolic acid powder with fine grains falling onto it"></div>

    <div class="free-from">
      <div class="percent">0%</div>
      <ul>
        <li>Fragrances</li>
        <li>Additives</li>
        <li>Dyes</li>
      </ul>
    </div>

    <div class="resealable">
      <svg width="28" height="34" viewBox="0 0 28 34" aria-hidden="true">
        <rect x="2" y="12" width="24" height="21" rx="2" fill="#ffffff"/>
        <rect x="4" y="1" width="6" height="9" fill="#ffffff"/>
        <rect x="11" y="1" width="6" height="9" fill="#ffffff"/>
        <rect x="18" y="1" width="6" height="9" fill="#ffffff"/>
        <rect x="9" y="19" width="10" height="7" fill="#2c6264"/>
      </svg>
      Resealable<br>Bag
    </div>

    <div class="net-weight">NET WT. 100G</div>
  </main>
</body>
</html>
```